Garlic Farm for Farm Sales/Restaurant sales

Need a professional, but appealing to agriculture world. We are selling 27 kinds of Organic Garlic from a farm in Simla,CO. I have uploaded logo and business information-we are going to need a template, because I will need to use it for four separate people.
-We are trying to appeal to Farm to table restaurants
-As well as growers/farmers

Target Market(s)

Agriculture Sales/Restaurants-Organic

Industry/Entity Type

Agriculture

Contact Information for Business Card

Want it to look more unique then your average brimly ink card- I want it to look amazing

Font styles to use
Sans Serif

Colors
0455a3
ec1f27
fbed22
ffffff

Requirements
Must have
• Just be creative
Nice to have
• Colorful
Should not have
• plain

```html
<!DOCTYPE html>
<html lang="en">
<head>
<meta charset="utf-8">
<title>Summit Ridge Garlic – Business Card</title>
<link href="https://fonts.googleapis.com/css2?family=Josefin+Sans:wght@400;600;700&display=swap" rel="stylesheet">
<style>
  :root {
    --navy: #1b2f5e;
    --red: #c8202f;
    --yellow: #fbd11c;
    --white: #ffffff;
    --stage: #2b2b2d;
  }
  * { box-sizing: border-box; margin: 0; padding: 0; }
  html, body { width: 1200px; height: 900px; overflow: hidden; background: var(--stage); }
  body { position: relative; font-family: "Josefin Sans", sans-serif; }

  .card {
    position: absolute;
    width: 640px;
    height: 366px;
    border-radius: 22px;
    overflow: hidden;
    box-shadow: 0 14px 30px rgba(0,0,0,.45);
  }

  /* Front (navy) */
  .card-front { left: 70px; top: 80px; background: var(--navy); }
  .card-front .band-red {
    position: absolute; left: 0; right: 0; top: 262px; height: 74px; background: var(--red);
  }
  .card-front .brand {
    position: absolute; right: 52px; top: 120px;
    display: flex; align-items: center; gap: 14px;
  }
  .brand-dot {
    width: 58px; height: 58px; border-radius: 50%; background: var(--red); flex: none;
  }
  .brand-name {
    font-weight: 700; font-size: 34px; letter-spacing: .5px; line-height: 1;
  }
  .card-front .brand-name { color: var(--white); }
  .social-row {
    position: absolute; right: 44px; top: 280px;
    display: flex; gap: 34px;
  }
  .social-dot {
    width: 34px; height: 34px; border-radius: 50%; background: var(--white);
  }

  /* Back (white) */
  .card-back { left: 490px; top: 474px; background: var(--white); }
  .card-back .wave { position: absolute; left: 0; top: 0; width: 640px; height: 366px; }
  .card-back .brand {
    position: absolute; right: 40px; top: 44px;
    display: flex; align-items: center; gap: 14px;
  }
  .card-back .brand-name { color: var(--navy); }
  .contact-list {
    position: absolute; right: 34px; top: 134px;
    list-style: none; text-align: right;
  }
  .contact-list li {
    display: flex; justify-content: flex-end; align-items: center; gap: 10px;
    color: var(--navy); font-size: 17px; line-height: 28px;
  }
  .contact-list .accent { color: var(--red); }
  .contact-icon {
    width: 18px; height: 18px; border-radius: 3px; background: var(--red);
    display: flex; align-items: center; justify-content: center;
  }
  .person-name {
    position: absolute; left: 36px; top: 226px;
    font-size: 32px; font-weight: 600; letter-spacing: 1.5px; color: var(--navy);
  }
  .person-name .surname { color: var(--red); }
  .address {
    position: absolute; left: 36px; top: 302px;
    font-size: 19px; color: var(--yellow);
  }
</style>
</head>
<body>

  <section class="card card-front" aria-label="Card front">
    <div class="band-red"></div>
    <div class="brand">
      <span class="brand-dot"></span>
      <span class="brand-name">Summit Ridge Garlic</span>
    </div>
    <div class="social-row" aria-label="Social links">
      <span class="social-dot"></span>
      <span class="social-dot"></span>
      <span class="social-dot"></span>
      <span class="social-dot"></span>
    </div>
  </section>

  <section class="card card-back" aria-label="Card back">
    <svg class="wave" viewBox="0 0 640 366" preserveAspectRatio="none" aria-hidden="true">
      <path d="M0 286 C150 226 300 300 440 250 C540 214 600 210 640 190 L640 366 L0 366 Z" fill="var(--yellow)"/>
      <path d="M0 296 C150 238 300 312 440 262 C540 226 600 222 640 204 L640 366 L0 366 Z" fill="var(--red)"/>
    </svg>
    <div class="brand">
      <span class="brand-dot"></span>
      <span class="brand-name">Summit Ridge Garlic</span>
    </div>
    <ul class="contact-list">
      <li>555-014-2298
        <span class="contact-icon">
          <svg width="11" height="11" viewBox="0 0 24 24"><path d="M6.6 10.8a15 15 0 0 0 6.6 6.6l2.2-2.2c.3-.3.7-.4 1-.2 1.1.4 2.3.6 3.6.6.6 0 1 .4 1 1V20c0 .6-.4 1-1 1A17 17 0 0 1 3 4c0-.6.4-1 1-1h3.5c.6 0 1 .4 1 1 0 1.3.2 2.5.6 3.6.1.3 0 .7-.2 1z" fill="#fff"/></svg>
        </span>
      </li>
      <li>Dana@SRGarlic.com
        <span class="contact-icon">
          <svg width="12" height="10" viewBox="0 0 24 18"><rect x="1" y="1" width="22" height="16" rx="2" fill="none" stroke="#fff" stroke-width="2"/><path d="M2 2l10 8 10-8" fill="none" stroke="#fff" stroke-width="2"/></svg>
        </span>
      </li>
      <li><span>www.<span class="accent">SR</span>Garlic.com</span>
        <span class="contact-icon">
          <svg width="12" height="12" viewBox="0 0 24 24"><circle cx="12" cy="12" r="10" fill="none" stroke="#fff" stroke-width="2"/><path d="M2 12h20M12 2c3 3 3 17 0 20M12 2c-3 3-3 17 0 20" fill="none" stroke="#fff" stroke-width="1.6"/></svg>
        </span>
      </li>
    </ul>
    <p class="person-name">DANA <span class="surname">WELLS</span></p>
    <p class="address">P.O. Box 12 Lindon, CO 80740</p>
  </section>

</body>
</html>
```